Flyer-Design für private Deutschschule
Zielgruppe
Wir sind eine private Deutschschule in München im gehobenen Segment und betreuen hauptsächlich Firmenkunden, die viele ausländische Mitarbeiter beschäftigen. Professionalität steht im Vordergrund mit jahrelanger Expertise im Spracherwerb.
Aufgabenstellung
• Six-sided, warp-fold/letterfold flyer
• Size DIN Lang
• With a cool and trendy design that looks very (oriented slightly on the curved design on our website varentobex.de)
• Keep in mind we will use the MUC (Munich) version for these flyers and therefor will be working with the #cc1e41 logo scheme.
• Please note that all information written in English is just for instructions and everything written in German can be used 1:1 for content.
So, I’d like to explain to you a bit about our ideas – however we are always hoping that you have some innovative, own ideas that can be used complementary. For both design and content you are free to browse through our website that I made with the Divi theme on Wordpress and some content is already short-scripted and easy to copy. You can translate the whole website by clicking on the top right part and changing it to various languages and like that evaluate by yourself what you think is reasonable to use.
Now all the information about the content:
The reasons why companies should have their own courses: “Stechen Sie heraus!”
Subtitle: “Ein Deutschkurs für Arbeitnehmer ist die perfekte Lösung für einen modernen Arbeitgeber:“
- Erweiterung des Angebots an Lohnnebenleistungen
- Steigerung der Zufriedenheit und des Engagements der Mitarbeiter
- Investition in die Mitarbeiterentwicklung und die Arbeitgebermarke
- Reduzierung der Kosten bei gleichzeitiger Erhöhung des Sprachtrainings
Then we have four more clusters:
- Branchenspezifisch: Alle Schulungen sind individuell auf Ihr Team zugeschnitten. Wir machen Ihnen vorab Vorschläge für einen ideal auf Ihr Unternehmen angepassten Kursablauf und stufen Ihre Mitarbeiter auf Wunsch ein.
- In Ihrer Firma vor Ort: Ihre Mitarbeiter werden von uns in Ihren Räumlichkeiten unterrichtet und können somit zwischen oder nach der Arbeit in einer gewohnten Umgebung Deutsch lernen. Sie ersparen Ihre..

```html
<!DOCTYPE html>
<html lang="de">
<head>
<meta charset="utf-8">
<title>Varentobex – Firmendeutschkurse Flyer</title>
<link href="https://fonts.googleapis.com/css2?family=Rubik:wght@300;400;500;700;800&display=swap" rel="stylesheet">
<style>
  :root {
    --red: #cc1e41;
    --red-light: #dc3a5c;
    --red-dark: #c4304f;
    --yellow: #ecb12a;
    --yellow-dark: #d69a1f;
    --grey-panel: #dcdcdc;
    --grey-panel-light: #e6e6e6;
    --ink: #3c3c3c;
    --ink-soft: #555555;
    --white: #ffffff;
    --page: #f2f2f2;
    --photo-warm: #c9b8a6;
    --photo-cool: #aab4c2;
  }
  * { margin: 0; padding: 0; box-sizing: border-box; }
  html, body {
    width: 878px; height: 1200px; overflow: hidden;
    background: var(--page);
    font-family: "Rubik", sans-serif;
    color: var(--ink);
  }
  .sheet {
    position: absolute; left: 49px; width: 780px; height: 552px;
    display: flex; box-shadow: 0 10px 24px rgba(0,0,0,.12);
  }
  .sheet--outside { top: 32px; }
  .sheet--inside { top: 616px; }
  .panel { position: relative; width: 260px; height: 100%; overflow: hidden; }
  .panel--white { background: var(--white); }
  .panel--red { background: linear-gradient(160deg, var(--red-light), var(--red-dark)); }
  .panel--grey { background: linear-gradient(180deg, var(--grey-panel), var(--grey-panel-light) 60%, var(--grey-panel)); }
  .panel--yellow { background: linear-gradient(170deg, var(--yellow), var(--yellow-dark)); }

  .photo { position: absolute; }
  .photo--team { left: 0; top: 146px; width: 250px; height: 186px;
    background: linear-gradient(135deg, var(--photo-cool), var(--photo-warm) 60%, #e7e2dc); }
  .photo--class { left: 8px; top: 240px; width: 252px; height: 188px;
    background: linear-gradient(135deg, #e9ecef, var(--photo-cool) 50%, #8f98a6); }
  .photo--learners { left: 288px; top: 80px; width: 492px; height: 292px;
    background: linear-gradient(120deg, #b59b84, #9aa7b5 55%, #dfe6ee); z-index: 2; }

  .accent-bar { position: absolute; width: 9px; }
  .accent-bar--yellow { left: 12px; top: 273px; height: 198px; background: var(--yellow); }
  .accent-bar--red { left: 8px; top: 162px; height: 142px; background: var(--red); width: 8px; }

  .benefits { position: absolute; left: 26px; top: 372px; width: 200px; list-style: none; }
  .benefits li { font-size: 7.6px; font-weight: 300; line-height: 1.4; color: var(--ink-soft); margin-bottom: 9px; }
  .growth-icon { position: absolute; right: 10px; bottom: 68px; }

  .contact { position: absolute; left: 30px; }
  .contact-row { display: flex; align-items: center; margin-bottom: 4px; }
  .contact-row svg { width: 26px; margin-right: 16px; }
  .pill {
    display: flex; align-items: center; justify-content: center; text-align: center;
    width: 156px; height: 29px; border-radius: 15px;
    font-size: 9.5px; font-weight: 700; line-height: 1.15;
  }
  .pill--white { background: var(--white); color: var(--red); }
  .pill--red { background: var(--red-light); color: var(--white); }
  .pill--two-line { font-size: 8px; line-height: 1.1; justify-content: flex-start; text-align: left; padding: 0 10px; }
  .contact--outside { top: 450px; }
  .contact--inside { top: 456px; left: 36px; }
  .contact--inside .pill { background: var(--red); color: var(--white); }

  .brand { position: absolute; right: 12px; top: 34px; text-align: right; }
  .brand-name { font-size: 15px; font-weight: 500; color: var(--red); display: flex; align-items: center; gap: 5px; }
  .brand-dot { width: 14px; height: 14px; border-radius: 50%; background: var(--red); }
  .brand-tag { font-size: 5px; letter-spacing: .3px; color: var(--ink-soft); margin-top: 2px; }
  .headline { position: absolute; left: 8px; top: 120px; font-size: 21px; font-weight: 700; color: var(--ink); letter-spacing: -.4px; white-space: nowrap; }
  .subline { position: absolute; left: 44px; top: 164px; width: 206px; font-size: 11px; font-weight: 700; line-height: 1.3; color: var(--red); }

  .features { position: absolute; left: 12px; top: 40px; width: 240px; }
  .feature { display: flex; margin-bottom: 22px; }
  .feature-icon { width: 60px; flex: none; display: flex; justify-content: center; padding-top: 2px; }
  .feature-icon .icon-slot { width: 40px; height: 36px; border-radius: 6px; background: #cfcfcf; }
  .feature h3 { font-size: 9.5px; font-weight: 700; letter-spacing: .4px; color: var(--red); margin-bottom: 1px; }
  .feature p { font-size: 7.4px; font-weight: 300; line-height: 1.4; color: var(--ink); }

  .offers { position: absolute; left: 52px; top: 402px; }
  .offers .pill { margin-bottom: 9px; }
</style>
</head>
<body>

<section class="sheet sheet--outside" aria-label="Flyer Außenseite">
  <div class="panel panel--white">
    <div class="photo photo--team" role="img" aria-label="Foto: lächelnde Kursteilnehmer an Tischen im Seminarraum"></div>
    <div class="accent-bar accent-bar--yellow"></div>
    <ul class="benefits">
      <li>Erweiterung des Angebots an Lohnnebenleistungen</li>
      <li>Steigerung der Zufriedenheit und des Engagements der Mitarbeiter</li>
      <li>Investition in die Mitarbeiterentwicklung und die Arbeitgebermarke</li>
      <li>Reduzierung der Kosten bei gleichzeitiger Erhöhung des Sprachtrainings</li>
    </ul>
    <svg class="growth-icon" width="50" height="48" viewBox="0 0 50 48" fill="none" stroke="#ecb12a" stroke-width="2" aria-hidden="true">
      <rect x="2" y="40" width="7" height="6" rx="1"/>
      <rect x="13" y="34" width="7" height="12" rx="1"/>
      <rect x="24" y="26" width="7" height="20" rx="1"/>
      <rect x="35" y="14" width="7" height="32" rx="1"/>
      <path d="M4 32 C18 28 26 20 30 4"/>
      <path d="M26 7 L30 2 L33 8"/>
    </svg>
  </div>

  <div class="panel panel--red">
    <div class="contact contact--outside">
      <div class="contact-row">
        <svg viewBox="0 0 26 26" fill="none" stroke="#fff" stroke-width="1.6" aria-hidden="true">
          <circle cx="13" cy="13" r="11"/><ellipse cx="13" cy="13" rx="5" ry="11"/>
          <path d="M2 13h22M4 7h18M4 19h18"/>
        </svg>
        <div class="pill pill--white">https://varentobex.de/</div>
      </div>
      <div class="contact-row">
        <svg viewBox="0 0 26 26" fill="none" stroke="#fff" stroke-width="1.6" aria-hidden="true">
          <path d="M7 3l4 5-2 3c1 3 3 5 6 6l3-2 5 4-2 4c-9 0-17-8-17-17z"/>
        </svg>
        <div class="pill pill--white">+49 89 000 482 19</div>
      </div>
    </div>
  </div>

  <div class="panel panel--grey">
    <div class="brand">
      <div class="brand-name"><span class="brand-dot"></span>VarentobexMUC</div>
      <div class="brand-tag">SPRACH- UND FIRMENKURSE</div>
    </div>
    <h1 class="headline">Stechen Sie heraus!</h1>
    <div class="accent-bar accent-bar--red"></div>
    <p class="subline">Ein Deutschkurs für Arbeitnehmer ist die perfekte Lösung für einen modernen Arbeitgeber</p>
    <div class="photo photo--class" role="img" aria-label="Foto: Gruppe junger Erwachsener beim Lernen in einem Kursraum"></div>
  </div>
</section>

<section class="sheet sheet--inside" aria-label="Flyer Innenseite">
  <div class="panel panel--grey">
    <div class="features">
      <div class="feature">
        <div class="feature-icon">
          <svg width="44" height="40" viewBox="0 0 44 40" fill="none" stroke="#3c3c3c" stroke-width="1.6" aria-hidden="true">
            <path d="M2 38V20l8-5v5l8-5v5l8-5v5l6-4V4h6v34z"/>
            <rect x="6" y="28" width="4" height="4"/><rect x="13" y="28" width="4" height="4"/>
            <rect x="20" y="28" width="4" height="4"/><path d="M27 38v-8h5v8"/>
            <path d="M33 1c2 0 2 2 4 2"/>
          </svg>
        </div>
        <div>
          <h3>BRANCHENSPEZIFISCH</h3>
          <p>Alle Schulungen sind individuell auf Ihr Team zugeschnitten. Wir machen Ihnen vorab Vorschläge für einen ideal auf Ihr Unternehmen angepassten Kursablauf und stufen Ihre Mitarbeiter auf Wunsch ein.</p>
        </div>
      </div>
      <div class="feature">
        <div class="feature-icon">
          <svg width="26" height="34" viewBox="0 0 26 34" fill="none" stroke="#3c3c3c" stroke-width="1.8" aria-hidden="true">
            <path d="M13 32C5 22 2 17 2 12a11 11 0 0 1 22 0c0 5-3 10-11 20z"/>
            <circle cx="13" cy="12" r="4.5"/>
          </svg>
        </div>
        <div>
          <h3>IN IHRER FIRMA VOR ORT</h3>
          <p>Ihre Mitarbeiter werden von uns in Ihren Räumlichkeiten unterrichtet und können somit zwischen oder nach der Arbeit in einer gewohnten Umgebung Deutsch lernen. Sie ersparen Ihren Mitarbeitern den Weg zur Sprachschule.</p>
        </div>
      </div>
      <div class="feature">
        <div class="feature-icon"><div class="icon-slot" role="img" aria-label="Liniensymbol: Team mit Vorgesetztem"></div></div>
        <div>
          <h3>SIE SIND DER CHEF</h3>
          <p>Sie bestimmen die Zeiten und den Rhythmus des Kurses. Somit gewährleisten Sie eine optimale Integration in Ihre Arbeitsprozesse. Regelmäßige Lernstandserhebungen und Evaluationen teilen wir mit Ihnen.</p>
        </div>
      </div>
      <div class="feature">
        <div class="feature-icon"><div class="icon-slot" role="img" aria-label="Liniensymbol: Person mit Buch und Häkchen"></div></div>
        <div>
          <h3>MEHRWERT SCHAFFEN</h3>
          <p>Ein individuell angepasster Deutschkurs erhöht die Sprachkompetenz Ihrer Mitarbeiter, was sich in der Qualität der Geschäftskontakte widerspiegelt. Zudem ermöglicht der handlungsorientierte Ansatz die Bewältigung von beruflichen Situationen.</p>
        </div>
      </div>
    </div>
    <div class="contact contact--inside">
      <div class="contact-row">
        <svg viewBox="0 0 26 26" fill="none" stroke="#cc1e41" stroke-width="1.6" aria-hidden="true">
          <circle cx="13" cy="13" r="11"/><ellipse cx="13" cy="13" rx="5" ry="11"/>
          <path d="M2 13h22M4 7h18M4 19h18"/>
        </svg>
        <div class="pill">https://varentobex.de/</div>
      </div>
      <div class="contact-row">
        <svg viewBox="0 0 26 26" fill="none" stroke="#cc1e41" stroke-width="1.6" aria-hidden="true">
          <path d="M7 3l4 5-2 3c1 3 3 5 6 6l3-2 5 4-2 4c-9 0-17-8-17-17z"/>
        </svg>
        <div class="pill">+49 89 000 482 19</div>
      </div>
    </div>
  </div>

  <div class="panel panel--yellow"></div>

  <div class="panel panel--white">
    <div class="offers">
      <div class="pill pill--red">kostenlos testen</div>
      <div class="pill pill--red">8 €/UE (MwSt befreit)</div>
      <div class="pill pill--red pill--two-line">innerhalb 24 Std. unverbind-<br>liches Angebot erhalten</div>
    </div>
  </div>

  <div class="photo photo--learners" role="img" aria-label="Foto: Kursteilnehmer unterschiedlichen Alters schreiben aufmerksam im Unterricht mit"></div>
</section>

</body>
</html>
```